Events Online Video Streaming Company

A website needs to be designed to replace the current website of a company that specialises in providing an online portal for streaming events to users. the current portal exists at: http://www.qulmora.com <- designers can get a "feel" for what they do and the content they require from this existing website.
the current qulmora logo and green color are to be maintined. i will upload an EPS of the logo soon.
The new design needs to highlight the main aspects of what they do: live streaming of events, multiple cameras, online chat, user activity data (like zintro dashtrack), customised front-ends.
we want the design to be in-between a corporate feel and modern, contemporary. ie. we dont want it to be too corporate (like the current website).
the design must also incorporate the word: glimmerfolk as part of their slogan or sub-title.
hi everyone,

```html
<!DOCTYPE html>
<html lang="en">
<head>
<meta charset="utf-8">
<title>Qulmora – Live Social Media Integrated Portal</title>
<link href="https://fonts.googleapis.com/css2?family=Source+Sans+3:wght@300;400;600;700&display=swap" rel="stylesheet">
<style>
:root{
  --green:#8cc63f;
  --green-band:#8dc641;
  --green-dark:#5e9e22;
  --green-text:#6aa824;
  --ink:#333333;
  --muted:#555555;
  --page:#f2f2f2;
  --card:#ffffff;
  --line:#dddddd;
  --footer:#2b2b2b;
  --step:#2a2a2a;
  --more-red:#8a1c1c;
}
*{box-sizing:border-box;margin:0;padding:0}
html,body{width:1200px;height:2335px;overflow:hidden}
body{position:relative;background:var(--page);font-family:"Source Sans 3",Arial,sans-serif;color:var(--ink)}
.abs{position:absolute}
.top-strip{left:0;top:0;width:1200px;height:18px;background:linear-gradient(#9a9a9a,#d8d8d8)}
.brand{left:100px;top:40px;width:260px;height:90px}
.brand-name{position:absolute;left:0;top:0;font-size:48px;font-weight:600;color:var(--ink);line-height:60px}
.brand-tag{position:absolute;left:148px;top:64px;font-size:18px;color:#222;font-weight:400}
.social{left:900px;top:35px;display:flex;gap:12px}
.social span{width:26px;height:26px;background:var(--green);border-radius:2px;display:block}
.search{left:853px;top:80px;width:237px;height:28px;display:flex}
.search-field{flex:1;border:1px solid #ccc;background:#fff;font-size:12px;font-style:italic;color:#777;padding:6px 10px}
.search-btn{width:38px;background:#555;display:flex;align-items:center;justify-content:center}
.nav{left:100px;top:137px;width:996px;height:54px;background:linear-gradient(#a3d45c,#72b232 60%,#5f9f28);display:flex;box-shadow:0 1px 2px rgba(0,0,0,.2)}
.nav a{color:#fff;text-decoration:none;font-size:14px;text-transform:uppercase;line-height:54px;padding:0 28px;border-right:1px solid rgba(255,255,255,.35)}
.nav a:first-child{padding-left:40px}
.nav a:last-child{border-right:0}
.hero{left:100px;top:210px;width:998px;height:362px;border:2px solid #fff;box-shadow:0 8px 10px -6px rgba(0,0,0,.55)}
.hero-photo{position:absolute;inset:0;background:linear-gradient(90deg,#6d6a55 0%,#5b4a3c 35%,#7a6e5e 55%,#9aa58d 80%,#c4cbbd 100%)}
.hero-panel{position:absolute;left:0;top:90px;width:350px;height:200px;background:rgba(25,25,25,.55);padding:20px 22px;color:#fff}
.hero-panel h1{font-size:19px;font-weight:400;line-height:29px}
.hero-panel p{font-size:11.5px;line-height:15px;margin-top:6px;color:#eee}
.btn-more{display:inline-block;margin-top:20px;width:88px;height:36px;border-radius:6px;background:linear-gradient(#9ed457,#6fb02f);color:#fff;font-size:16px;line-height:36px;padding-left:15px}
.hero-dots{position:absolute;left:428px;top:326px;width:142px;height:34px;background:#333;border-radius:12px 12px 0 0;display:flex;gap:12px;justify-content:center;align-items:center}
.hero-dots i{width:12px;height:12px;border-radius:50%;background:#888;display:block}
.hero-dots i:first-child{background:var(--green)}
.section-title{font-size:22px;font-weight:400;color:#222}
.cat-card{width:312px;height:151px;background:var(--card);border:1px solid var(--line);box-shadow:0 1px 2px rgba(0,0,0,.08);padding:10px 20px}
.cat-card h3{font-size:20px;font-weight:600;color:var(--green-text)}
.cat-icon{position:absolute;left:22px;top:52px;width:52px;height:52px;border-radius:8px}
.cat-card p{position:absolute;left:110px;top:48px;width:185px;font-size:12px;line-height:16px;color:#444;text-align:justify}
.cat-more{position:absolute;right:16px;bottom:16px;font-size:11px;font-weight:700;color:var(--green-text)}
.cat-more b{color:#333;font-weight:600}
.services{left:0;top:1046px;width:1200px;height:806px;background:var(--green-band);color:#fff}
.svc{width:240px;text-align:center}
.svc h4{font-size:19px;font-weight:600}
.svc-circle{position:relative;width:156px;height:156px;margin:18px auto 0;border-radius:50%;background:#fff;overflow:hidden;box-shadow:0 0 0 3px rgba(0,0,0,.1),0 4px 6px rgba(0,0,0,.25)}
.svc-circle .ico{position:absolute;left:48px;top:30px;width:60px;height:50px;border-radius:8px}
.svc-circle .step{position:absolute;left:0;bottom:0;width:100%;height:52px;background:var(--step);font-size:15px;font-weight:700;line-height:40px}
.svc p{font-size:12.5px;line-height:18px;margin:20px auto 0;width:182px;color:#1f2d10}
.features-title{color:var(--green-text);font-size:22px;font-weight:600}
.arrow{width:27px;height:27px;border-radius:50%;background:#222;display:flex;align-items:center;justify-content:center}
.feat{width:205px}
.feat h5{font-size:17px;font-weight:400;color:#111}
.feat-img{margin-top:10px;width:205px;height:74px;border:1px solid #ccc}
.feat p{margin-top:10px;font-size:11.5px;line-height:16px;color:#444;text-align:justify}
.feat .more{position:absolute;top:205px;font-size:11.5px;color:var(--more-red)}
.footer{left:0;top:2180px;width:1200px;height:155px;background:var(--footer);color:#ddd}
.footer h6{position:absolute;left:128px;top:18px;font-size:19px;font-weight:400;color:#fff}
.footer ul{position:absolute;top:58px;list-style:none;font-size:11.5px;line-height:17.5px;color:#ccc}
.copyright{position:absolute;right:140px;top:32px;font-size:11px;color:#ccc}
</style>
</head>
<body>
<div class="abs top-strip"></div>

<div class="abs brand">
  <div class="brand-name">Qulmora</div>
  <div class="brand-tag">Glimmerfolk</div>
</div>

<div class="abs social" aria-label="Social links"><span></span><span></span><span></span><span></span><span></span></div>
<div class="abs search">
  <div class="search-field">Search</div>
  <div class="search-btn"><svg width="16" height="16" viewBox="0 0 16 16"><circle cx="6.5" cy="6.5" r="4.5" fill="none" stroke="#fff" stroke-width="2"/><line x1="10" y1="10" x2="14.5" y2="14.5" stroke="#fff" stroke-width="2.4"/></svg></div>
</div>

<nav class="abs nav">
  <a>Home</a><a>Features</a><a>Applications</a><a>The Team</a><a>Support</a><a>Contact Us</a>
</nav>

<section class="abs hero">
  <div class="hero-photo" role="img" aria-label="Photo of a young woman looking at her mobile phone on a busy street"></div>
  <div class="hero-panel">
    <h1>Welcome to Qulmora a Live<br>Social&nbsp; Media Integrated Portal</h1>
    <p>Sed ut perspiciatis unde omnis iste natus error sit volupta-<br>tem accusantium doloremque laudantium, totam rem<br>aperiam, eaque ipsa quae ab illo inventore veritatis</p>
    <span class="btn-more">More</span>
  </div>
  <div class="hero-dots"><i></i><i></i><i></i><i></i></div>
</section>

<h2 class="abs section-title" style="left:104px;top:613px">Categories</h2>

<div class="abs cat-card" style="left:104px;top:667px"><h3>Education</h3><div class="cat-icon" role="img" aria-label="Graduation cap and diploma icon" style="background:#3a3a3a"></div><p>With much of todays learning being based off campus, Qulmora is an effective educational tool.</p><span class="cat-more">MORE <b>&gt;&gt;</b></span></div>
<div class="abs cat-card" style="left:446px;top:667px"><h3>Sport</h3><div class="cat-icon" role="img" aria-label="Basketball on a wooden court icon" style="background:#9a4a22"></div><p>View live sports events, check out the stats, and chat with friends about the game.</p><span class="cat-more">MORE <b>&gt;&gt;</b></span></div>
<div class="abs cat-card" style="left:786px;top:667px"><h3>Communications Solutions</h3><div class="cat-icon" role="img" aria-label="Green network globe with gears icon" style="background:#7bb84a"></div><p>Qulmora is a great communication tool for business with broadcast, discussion and feedback systems built in.</p><span class="cat-more">MORE <b>&gt;&gt;</b></span></div>
<div class="abs cat-card" style="left:104px;top:847px"><h3>Gigs and Festivals</h3><div class="cat-icon" role="img" aria-label="Group of people icon" style="background:#5d7ea8"></div><p>What to see a band but its sold out, watch it live online, while chatting with your friends.</p><span class="cat-more">MORE <b>&gt;&gt;</b></span></div>
<div class="abs cat-card" style="left:446px;top:847px"><h3>Conferences</h3><div class="cat-icon" role="img" aria-label="Globe on a stand icon" style="background:#3e6fb8"></div><p>Too busy to attend the event, attend virtually instead and don't miss out on content or social.</p><span class="cat-more">MORE <b>&gt;&gt;</b></span></div>
<div class="abs cat-card" style="left:786px;top:847px"><h3>What Else</h3><div class="cat-icon" role="img" aria-label="Light bulb icon" style="background:#e4e4e4"></div><p>Qulmora has a multitude of uses with many ideas in development. Have an idea? Drop us a line.</p><span class="cat-more">MORE <b>&gt;&gt;</b></span></div>

<section class="abs services">
  <h2 class="abs section-title" style="left:104px;top:20px;color:#fff">Our Services</h2>

  <div class="abs svc" style="left:88px;top:70px"><h4>Innovation / Technology</h4><div class="svc-circle"><div class="ico" role="img" aria-label="Blue cloud icon" style="background:#2f8fdc"></div><div class="step">Step 1</div></div><p>Developments such as mobile devices, mobile internet, video streaming, cloud computing, and web development systems have made it possible for us to develop Qulmora with the use of the lastest innovative technologies.</p></div>
  <div class="abs svc" style="left:342px;top:70px"><h4>Social Media, Networking</h4><div class="svc-circle"><div class="ico" role="img" aria-label="Cluster of social app icons" style="background:#6a8ab8"></div><div class="step">Step 2</div></div><p>Users can engage with the event by integrating their existing social networking accounts allowing them to see their connections and establish professional rela-tionships and discussion.</p></div>
  <div class="abs svc" style="left:603px;top:70px"><h4>Live Video Streaming</h4><div class="svc-circle"><div class="ico" role="img" aria-label="Television screen with colourful icons" style="background:#2b3b5a"></div><div class="step">Step 3</div></div><p>High quality live video streaming means you get to see the event as it happens without waiting for a stream to buffer. Qulmora offers a choice of different resolutions to suit your connection speed.</p></div>
  <div class="abs svc" style="left:865px;top:70px"><h4>Video on Demand</h4><div class="svc-circle"><div class="ico" role="img" aria-label="Film clapperboard icon" style="background:#2a2a2a"></div><div class="step">Step 4</div></div><p>Developments such as mobile devices, mobile internet, video streaming, cloud computing, and web development systems have made it possible for us to develop Qulmora with the use of the lastest innovative technologies.</p></div>

  <div class="abs svc" style="left:88px;top:442px"><h4>Analytical Reporting</h4><div class="svc-circle"><div class="ico" role="img" aria-label="Rising chart board icon" style="background:#3a3a3a"></div><div class="step">Step 5</div></div><p>Qulmora includes detailed report-ing in realtime so you know who, when, where, why, how and for how long. You'll find out what works, and how to improve or tailor the content to make it even better.</p></div>
  <div class="abs svc" style="left:342px;top:442px"><h4>Sponsor/Advertising</h4><div class="svc-circle">
    <svg class="ico" style="left:52px;top:32px;width:54px;height:48px" viewBox="0 0 54 48"><line x1="20" y1="4" x2="27" y2="12" stroke="#29a9d6" stroke-width="3"/><line x1="34" y1="4" x2="27" y2="12" stroke="#29a9d6" stroke-width="3"/><rect x="3" y="12" width="48" height="32" rx="5" fill="none" stroke="#29a9d6" stroke-width="4"/><rect x="10" y="19" width="26" height="18" fill="#29a9d6"/><circle cx="43" cy="24" r="2.5" fill="#29a9d6"/></svg>
    <div class="step">Step 6</div></div><p>Qulmora is secure and allows event organisers to diversify their event income streams by adding revenue from virtual delegates as well as industry partners or sponsors of the event portal.</p></div>
  <div class="abs svc" style="left:603px;top:442px"><h4>Any Device, No Install</h4><div class="svc-circle"><div class="ico" role="img" aria-label="Laptop with globe icon" style="background:#8aa8c8"></div><div class="step">Step 7</div></div><p>High quality live video streaming means you get to see the event as it happens without waiting for a stream to buffer. Qulmora offers a choice of different resolutions to suit your connection speed.</p></div>
  <div class="abs svc" style="left:865px;top:442px"><h4>Easy To Use</h4><div class="svc-circle">
    <svg class="ico" style="left:54px;top:30px;width:48px;height:48px" viewBox="0 0 48 48"><circle cx="24" cy="24" r="22" fill="#5db82e"/><path d="M13 25 L21 33 L36 16" fill="none" stroke="#fff" stroke-width="5" stroke-linecap="round" stroke-linejoin="round"/></svg>
    <div class="step">Step 8</div></div><p>Everything about Qulmora is easy to use, but configurable and customisable for the advanced user. Click-by-click anyone can access and enjoy the content or the event.</p></div>
</section>

<h2 class="abs features-title" style="left:106px;top:1864px">Features</h2>
<div class="abs arrow" style="left:985px;top:1868px"><svg width="10" height="10" viewBox="0 0 10 10"><path d="M7 1 L3 5 L7 9" fill="none" stroke="#fff" stroke-width="2"/></svg></div>
<div class="abs arrow" style="left:1018px;top:1868px"><svg width="10" height="10" viewBox="0 0 10 10"><path d="M3 1 L7 5 L3 9" fill="none" stroke="#fff" stroke-width="2"/></svg></div>

<div class="abs feat" style="left:113px;top:1918px"><h5>Secure Event Content</h5><div class="feat-img" role="img" aria-label="Conference hall audience photo" style="background:linear-gradient(#6b4a1e,#c89a42)"></div><p>Qulmora allows event organisers to diver-sify their event income streams by adding revenue from virtual delegates as well as industry partners or sponsors of the event portal.</p><span class="more">More &gt;&gt;</span></div>
<div class="abs feat" style="left:364px;top:1918px"><h5>Latest Technology</h5><div class="feat-img" role="img" aria-label="Hand touching a digital interface photo" style="background:linear-gradient(90deg,#1e4e78,#5aa2d0)"></div><p>Qulmora combines the very latest tech-nologies into a portal that now makes it possible to attend an event online, while still getting many of the benefits of onsite attendance.</p><span class="more">More &gt;&gt;</span></div>
<div class="abs feat" style="left:605px;top:1918px"><h5>Too Busy to Attend?</h5><div class="feat-img" role="img" aria-label="Businessman with a glowing globe photo" style="background:linear-gradient(90deg,#1c1c1c,#6e6e6e)"></div><p>With Qulmora you can stay at home or the office and fit the event into your schedule, your work, and your life without missing out.</p><span class="more">More &gt;&gt;</span></div>
<div class="abs feat" style="left:847px;top:1918px"><h5>Global Audience</h5><div class="feat-img" role="img" aria-label="Group of business people photo" style="background:linear-gradient(#d8dde4,#4a5568)"></div><p>With Qulmora anyone in the world becomes a potential attendee, without the need to travel long distances at great expense.</p><span class="more">More &gt;&gt;</span></div>

<footer class="abs footer">
  <h6>Site Map</h6>
  <ul style="left:133px"><li>Communications</li><li>Conferences and conventions</li><li>Education and training</li><li>Festivals and Gigs</li></ul>
  <ul style="left:334px"><li>Live video streaming</li><li>Sporting Events</li><li>Welcome!</li><li>Features</li></ul>
  <ul style="left:475px"><li>Applications</li><li>The Team</li><li>Support</li><li>Contact Us</li></ul>
  <div class="copyright">© 2013 Qulmora.com,All Rights Reserved</div>
</footer>
</body>
</html>
```